Brochure Design Project

I would like for it took look a little different than my website, elegant, and classy. Our company wants to draw upper class customers to care for their home. We also focus private water taxi services for businesses to taxi their employees.

Target Market(s)

tourists, seasonal residents, property management.

Industry/Entity Type

Professional Service

Font styles to use
Serif

Requirements
Must have
• 2 sides

```html
<!DOCTYPE html>
<html lang="en">
<head>
<meta charset="utf-8">
<title>Cayo Palma Concierge Services – Trifold Brochure</title>
<link href="https://fonts.googleapis.com/css2?family=Open+Sans:wght@400;600;700;800&display=swap" rel="stylesheet">
<style>
:root{
  --coral:#f05a5b;
  --ink-dark:#241d1a;
  --panel-mid:#332924;
  --text-light:#e9e4e0;
  --text-body:#d8d2cd;
  --rule:#8d8480;
  --page:#dcdcdc;
  --white:#ffffff;
}
*{box-sizing:border-box;margin:0;padding:0}
html,body{width:840px;height:1200px;overflow:hidden}
body{background:var(--page);font-family:'Open Sans',sans-serif;color:var(--text-body);position:relative}
.sheet{position:absolute;left:20px;width:800px;height:580px;display:flex;box-shadow:0 3px 10px rgba(0,0,0,.35)}
.sheet--outside{top:12px;background:linear-gradient(100deg,#2b211d 0%,#3b2e27 45%,#2e2420 100%)}
.sheet--inside{top:608px;background:linear-gradient(160deg,#2e2521 0%,#2a2422 55%,#232a1f 100%)}
.panel{width:266.67px;height:100%;padding:22px 24px;position:relative;border-right:1px solid rgba(255,255,255,.05)}
.panel:last-child{border-right:none}
.heading{font-size:17px;font-weight:400;color:var(--coral);padding-bottom:6px;border-bottom:1px solid var(--rule);margin-bottom:12px}
.heading strong{font-weight:700}
.body-text{font-size:8.6px;line-height:11.4px;text-align:justify;color:var(--text-body);margin-bottom:16px}
.tagline{color:var(--coral);font-weight:700;font-size:13.5px;line-height:19px;text-align:center;margin:0 10px 12px}
.membership{color:var(--white);text-align:center;font-size:18px;line-height:22px;margin-top:28px}
.membership strong{font-weight:800;display:block}
.submit{color:var(--white);text-align:center;font-size:11px;margin-top:22px}
.submit a{display:block;color:var(--coral);font-weight:700;font-size:13.5px;margin-top:3px;text-decoration:none}
.call-icon{display:block;margin:14px auto -12px;position:relative;z-index:2}
.call-box{position:relative;border:1.5px solid var(--white);margin:0 6px;padding:14px 8px 18px;text-align:center;color:var(--white);font-weight:600;font-size:14.5px;line-height:20px}
.call-box .phone{position:absolute;left:50%;bottom:-14px;transform:translateX(-50%);white-space:nowrap;padding:0 6px;background:var(--panel-mid);color:var(--coral);font-weight:700;font-size:20px;line-height:26px}
.contact{color:var(--white);text-align:center;font-size:12px;margin-top:30px;line-height:26px}
.contact b{color:var(--coral);font-weight:700}
.cover{padding:0;overflow:hidden;background:var(--coral)}
.cover-top{height:140px;background:linear-gradient(100deg,#3a2d27,#2f2520);text-align:center;padding-top:14px}
.brand-mark{display:block;margin:0 auto 12px}
.brand-name{color:var(--text-light);font-size:16px;letter-spacing:3.5px;line-height:29px;font-weight:400}
.cover-art{position:absolute;left:0;top:120px;width:266.67px;height:370px}
.cover-headline{position:absolute;left:38px;top:180px;line-height:1}
.cover-headline .l1{color:var(--white);font-size:24px;font-weight:400}
.cover-headline .l2{color:var(--white);font-size:33px;font-weight:800}
.cover-headline .l3{color:var(--ink-dark);font-size:27px;font-weight:800}
.cover-phone{position:absolute;left:0;right:0;top:500px;text-align:center;color:var(--white);font-weight:700;font-size:27px}
.cover-url{position:absolute;left:0;right:0;top:538px;text-align:center;color:var(--white);font-size:13px}
.cover-url b{font-weight:700}
.section-title{font-size:21px;color:var(--coral);font-weight:400;padding-bottom:6px;border-bottom:1px solid var(--rule)}
.section-title strong{font-weight:700}
.service-icon{display:block;margin:0 auto}
.service-title{text-align:center;color:var(--coral);font-size:15.5px;font-weight:400;padding-bottom:8px;margin:8px 0 12px;border-bottom:1px solid var(--rule);position:relative;white-space:nowrap}
.service-title strong{font-weight:700}
.service-title::after{content:"";position:absolute;left:50%;bottom:-4px;margin-left:-4px;border:4px solid transparent;border-bottom:none;border-top-color:var(--white)}
.ticks{list-style:none;color:var(--white);font-size:12px;line-height:19px;margin-bottom:20px}
.ticks li{position:relative;padding-left:17px}
.ticks li::before{content:"✓";position:absolute;left:0;color:var(--coral);font-weight:700}
.ticks--vessel{font-size:11.2px;line-height:15px}
.ticks--vessel li{margin-bottom:4px}
.ticks--small{font-size:8.2px;line-height:10.8px;margin-bottom:10px}
.ticks--small li{padding-left:11px;margin-bottom:3px}
.ticks--small li::before{font-size:9px}
.sub-heading{font-size:15px;color:var(--coral);font-weight:400;padding-bottom:5px;border-bottom:1px solid var(--rule);margin-bottom:9px}
.sub-heading strong{font-weight:700}
.body-small{font-size:8px;line-height:10.8px;text-align:justify;margin-bottom:10px}
.membership-panel{background:linear-gradient(180deg,#3c2e28 0%,#2b2523 100%)}
</style>
</head>
<body>

<section class="sheet sheet--outside" aria-label="Brochure outside">
  <div class="panel">
    <h2 class="heading">About <strong>Us</strong></h2>
    <p class="body-text">Founded in 2017 by Daniel and Marisa Hollend, Cayo Palma Concierge provides the Palma Key area with an exclusive list of services for property management including home services, rental guest liaison, and membership services. We also offer private charters for water transportation to barrier islands, exclusive fishing adventures, and sightseeing tours.</p>
    <h2 class="heading">Marisa <strong>Hollend</strong></h2>
    <p class="body-text">As co-owner and operator of Cayo Palma Concierge, Marisa brings a strong professional background in client care together with a genuine passion for looking after people in the community. She studied at a regional college and built her career in service coordination, where she learned how much thoughtful planning matters. Over many years in demanding roles she has managed schedules, teams and resources with calm attention to detail. Today she brings that same care to every home and every guest. During her free time, she enjoys time on the water and quiet evenings with her family.</p>
    <h2 class="heading">Daniel <strong>Hollend</strong></h2>
    <p class="body-text">With a strong corporate background and years spent in large, customer-facing organizations, Daniel knows the importance of providing top level customer service. He began his career in a hands-on technical trade, earning his qualifications through steady practice and training. Now focused full time on the company, he has long pursued his passion for sport fishing, where he built lasting professional relationships with captains and guides throughout the islands he calls home.</p>
  </div>

  <div class="panel">
    <p class="body-text" style="margin-top:14px">Serving Palma Key and surrounding sister islands, Cayo Palma concierge is the top innovator in the concierge service industry. Concierge services are tailored to each request ensuring an exceptional client experience. We have the knowledge and resources through our trusted network of service providers to meet your individual needs and preferences.</p>
    <p class="tagline">Concierge Services Have Grown Far Beyond That of A Hotel Lobby.</p>
    <p class="tagline">Call Us With Your Request And CPC Will Do The Rest!</p>
    <p class="membership">ASK ABOUT OUR <strong>MEMBERSHIP RATES</strong></p>
    <p class="submit">SUBMIT A REQUEST ON OUR WEBSITE <a>CPCatYourService.com</a></p>
    <svg class="call-icon" width="30" height="30" viewBox="0 0 30 30" aria-hidden="true">
      <circle cx="15" cy="15" r="14" fill="#fff"/>
      <circle cx="15" cy="15" r="12" fill="none" stroke="#f05a5b" stroke-width="1.5"/>
      <path d="M10.5 8.5l3 3-1.6 1.6c.8 1.8 2.2 3.2 4 4l1.6-1.6 3 3-1.8 1.8c-4.5-.4-9.6-5.5-10-10z" fill="#f05a5b"/>
    </svg>
    <div class="call-box">Call and Speak With a Concierge Specialist <span class="phone">(555) 014-2290</span></div>
    <p class="contact">CPCatYourService@mailbox.com<br>www.<b>cpcatyourservice</b>.com</p>
  </div>

  <div class="panel cover">
    <div class="cover-top">
      <svg class="brand-mark" width="30" height="30" viewBox="0 0 30 30" aria-hidden="true"><circle cx="15" cy="15" r="13" fill="none" stroke="#e9e4e0" stroke-width="1.5"/></svg>
      <p class="brand-name">CAYO PALMA CONCIERGE<br>SERVICES L.L.C.</p>
    </div>
    <svg class="cover-art" viewBox="0 0 266.67 370" preserveAspectRatio="none">
      <defs>
        <linearGradient id="bellScene" x1="0" y1="0" x2="1" y2="1">
          <stop offset="0" stop-color="#3d6e96"/>
          <stop offset=".45" stop-color="#a9c3d8"/>
          <stop offset=".75" stop-color="#6c7c88"/>
          <stop offset="1" stop-color="#d7d7d7"/>
        </linearGradient>
      </defs>
      <path d="M0 20 C80 -5 190 -5 266.67 10 L266.67 345 C190 320 80 330 0 345 Z" fill="#f05a5b"/>
      <path d="M0 40 C80 12 190 10 266.67 22 L266.67 328 C190 305 80 312 0 330 Z" fill="url(#bellScene)" role="img" aria-label="Photograph of a polished silver service bell on a counter with blurred blue lights behind"/>
    </svg>
    <div class="cover-headline">
      <div class="l1">YOUR</div>
      <div class="l2">REQUEST IS</div>
      <div class="l3">OUR DEMAND</div>
    </div>
    <div class="cover-phone">(555) 014-2290</div>
    <div class="cover-url">www.<b>cpcatyourservice</b>.com</div>
  </div>
</section>

<section class="sheet sheet--inside" aria-label="Brochure inside">
  <div class="panel">
    <h2 class="section-title">OUR <strong>SERVICES</strong></h2>
    <svg class="service-icon" width="42" height="42" viewBox="0 0 42 42" style="margin-top:14px" role="img" aria-label="Fishing charters icon"><circle cx="21" cy="21" r="20" fill="#f05a5b" stroke="#fff" stroke-width="1"/></svg>
    <h3 class="service-title">FISHING <strong>CHARTERS</strong></h3>
    <p class="body-text">Our Concierge Captains provide a first-class fishing experience that you'll always remember! Some of the most popular daily catches could include: Tarpon, Snook, Trout, Grouper, Snapper, and our captains' personal favorite... the elusive "Red" Drum.</p>
    <ul class="ticks">
      <li>Full Day /Half Day</li>
      <li>Inshore/ Offshore</li>
      <li>Beach Shelling</li>
      <li>Prosecco Sunset Cruises</li>
      <li>Island Lunch Excursions</li>
    </ul>
    <p class="body-text" style="margin-bottom:10px">CPC also offers concierge guided services for businesses or avid fisherman out there looking to be a part of our local competitive fishing tournaments. Services provided for tournaments are all- inclusive and tailored to your specific requests.</p>
    <p class="body-text">We provide private water transportation to Heron Key, Pelican Point, Mangrove Key, for residents and business employees. Transport arrangement times are flexible taking the worry out of missing the boat!</p>
  </div>

  <div class="panel">
    <svg class="service-icon" width="42" height="42" viewBox="0 0 42 42" style="margin-top:14px" role="img" aria-label="Private vessel icon"><circle cx="21" cy="21" r="20" fill="#f05a5b" stroke="#fff" stroke-width="1"/></svg>
    <h3 class="service-title" style="margin-top:22px">PRIVATE <strong>VESSEL SERVICES</strong></h3>
    <p class="body-text" style="margin-top:16px">If you're searching for an awesome fishing experience, but would like to be catered to on your own boat, then you got it! We only employ reputable licensed Captains take care of your vessel. Catering to your vessel is a simple solution that allows you to spend more time on the water without hassling with work that goes with it.</p>
    <p class="body-text">Prefer to run your own boat, but would like us to take care of everything else? Let our Concierge staff handle all the preparations. Prior to your return, contact your Concierge Captain and we'll take it from there!</p>
    <ul class="ticks ticks--vessel">
      <li>Fuel</li>
      <li>On the Water Delivery</li>
      <li>Hauling</li>
      <li>Regularly Scheduled Cleaning</li>
      <li>Complete Detail &amp; Wax</li>
      <li>Cooler Stocked &amp; Beverages/ Food Items of Your Choice</li>
      <li>Interior Cleaning &amp; Detailing</li>
      <li>Schedule Engine Service &amp; Maintenance</li>
      <li>Custom Tailored Service Packages to Fit Your Needs</li>
    </ul>
  </div>

  <div class="panel membership-panel">
    <h3 class="sub-heading">Home <strong>Membership Services</strong></h3>
    <p class="body-small">As dedicated customer service specialists, we take pride in our performance. We aim to provide proficient solutions to take care of your home so you can have more time doing the things you enjoy. Our memberships are designed to keep your home functioning at its best. Pick and choose services personalized for your membership.</p>
    <ul class="ticks ticks--small">
      <li>Weekly, Bi-Weekly, Or Monthly Home Inspections</li>
      <li>Email &amp; Digital Reporting of General Home Maintenance Issues</li>
      <li>Year- Round Property Management for Full-Time &amp; Seasonal Residents</li>
      <li>Lawn Maintenance</li>
      <li>Scheduling Vendors/Contractors, With On-Site Supervision</li>
      <li>Home Improvement Solutions</li>
      <li>Managing Rental Turnover &amp; Maintenance</li>
      <li>Rental Property Guest Liaison</li>
    </ul>
    <h3 class="sub-heading">Home <strong>Arrival Preparations</strong></h3>
    <ul class="ticks ticks--small">
      <li>AC Thermostat Set to Personal Preference</li>
      <li>Ensure Adequate Lighting for Evening Arrivals</li>
      <li>Fluff &amp; Buff Cleaning (Light Dusting &amp; Dry Mop Floors)</li>
      <li>Turn on Hot Water Heater</li>
      <li>Food &amp; Household Items Purchased &amp; Stocked (Additional Fee)</li>
      <li>Housekeeping Services (Additional Fee)</li>
    </ul>
    <h3 class="sub-heading">Departure <strong>Services</strong></h3>
    <ul class="ticks ticks--small">
      <li>Set AC Thermostat to Energy Efficient Temperature</li>
      <li>Secure Windows &amp; Doors</li>
      <li>Turn Off Hot Water Heater</li>
      <li>Activate &amp; Check Security System</li>
      <li>Garbage Removal</li>
      <li>House Cleaning (Additional Fee)</li>
    </ul>
  </div>
</section>

</body>
</html>
```